CPA Firm Stationary & Business Cards
Whitfield & Partners CPAs PSC
CPA Firm Stationary & Business Cards - Financial Services
Creative Brief
Professional
Martin L. Dowse, CPA
Shareholder
4815 Tillamore Ave. Suite 1 Owensboro, KY 42303
mdowse@wpfcpa.net
www.wpfcpa.net
We are a CPA (Certified Public Accountant) firm, in business since 1924. In addition to Business Cards, I would also like to see designs for Letterheads and Envelopes.
Your choice. At a minimum, it should include the "W" logo.In addition to Business Cards, I would also like to see designs for Letterheads and Envelopes.

```html
<!DOCTYPE html>
<html lang="en">
<head>
<meta charset="utf-8">
<title>Whitfield &amp; Partners CPAs PSC — Stationery</title>
<link href="https://fonts.googleapis.com/css2?family=Montserrat:wght@400;600;700&display=swap" rel="stylesheet">
<style>
:root{
  --stage:#e9e7e3;
  --paper:#ffffff;
  --brand:#2552b8;
  --brand-deep:#163a8c;
  --brand-light:#6f94e0;
  --ink:#5a6170;
  --flap-grey:#8c8f96;
  --shadow:rgba(0,0,0,.18);
}
*{margin:0;padding:0;box-sizing:border-box}
html,body{width:1200px;height:466px;overflow:hidden}
body{background:var(--stage);font-family:"Montserrat",sans-serif;color:var(--ink);position:relative}
.piece{position:absolute;background:var(--paper);box-shadow:0 2px 6px var(--shadow);overflow:hidden}
.wordmark{color:var(--brand);font-weight:700;letter-spacing:.06em;line-height:1.15;text-transform:uppercase}
.wordmark small{display:block;font-size:.55em;letter-spacing:.04em}
.band{position:absolute;right:0;bottom:0;width:100%;height:100%;pointer-events:none}
.contact{font-size:4.2px;line-height:1.7;color:var(--ink)}
.contact i{display:inline-block;width:3px;height:3px;border-radius:50%;background:var(--brand);margin-right:3px;vertical-align:middle}

/* business cards */
.card-front{left:16px;top:306px;width:74px;height:42px;padding:6px}
.card-front .wordmark{font-size:5px}
.card-front .contact{font-size:2.6px;margin-top:4px}
.card-back{left:16px;top:360px;width:74px;height:52px;background:linear-gradient(135deg,var(--brand-light),var(--brand) 55%,var(--brand-deep))}

/* letterheads */
.letterhead{top:19px;width:308px;height:425px}
.letterhead-one{left:100px}
.letterhead-two{left:425px}
.letterhead-one .wordmark{position:absolute;left:22px;top:22px;font-size:11px}
.letterhead-one .contact{position:absolute;left:196px;top:20px}
.letterhead-two .wordmark{position:absolute;left:0;right:0;top:24px;text-align:center;font-size:12px}
.letterhead-two .contact{position:absolute;left:0;right:0;bottom:26px;text-align:center}
.letterhead-two .contact span{margin:0 5px}

/* envelopes */
.envelope{left:766px;width:380px;height:122px}
.env-back-blue{top:24px;background:var(--paper)}
.env-back-grey{top:140px}
.env-back-white{top:250px}
.env-front{top:352px;height:94px}
.flap{position:absolute;left:0;top:0;width:100%;height:100%}
.env-back-blue .wordmark{position:absolute;left:0;right:0;top:28px;text-align:center;font-size:8px;color:#fff}
.env-back-grey .wordmark,.env-back-white .wordmark{position:absolute;left:0;right:0;top:30px;text-align:center;font-size:7px}
.env-front .wordmark{position:absolute;left:14px;top:10px;font-size:8px}
.env-front .contact{position:absolute;left:14px;top:34px;font-size:3.6px}
</style>
</head>
<body>

<!-- business card front -->
<section class="piece card-front" aria-label="Business card front">
  <p class="wordmark">Whitfield<small>&amp; Partners CPAs PSC</small></p>
  <p class="contact">Martin L. Dowse, CPA · Shareholder<br>270.555.0142 · mdowse@wpfcpa.net<br>www.wpfcpa.net</p>
</section>

<!-- business card back -->
<section class="piece card-back" aria-label="Business card back"></section>

<!-- letterhead option one -->
<section class="piece letterhead letterhead-one" aria-label="Letterhead option one">
  <p class="wordmark">Whitfield<small>&amp; Partners CPAs PSC</small></p>
  <p class="contact">
    <i></i>4815 Tillamore Ave. Suite 1<br>
    <i></i>Owensboro, KY 42303<br>
    <i></i>270.555.0142<br>
    <i></i>270.555.0198<br>
    <i></i>www.wpfcpa.net
  </p>
  <svg class="band" viewBox="0 0 308 425" preserveAspectRatio="none" aria-hidden="true">
    <path d="M150 425 C220 418 270 410 308 396 L308 425 Z" fill="var(--brand)"/>
    <path d="M190 425 C250 420 285 414 308 406 L308 425 Z" fill="var(--brand-deep)"/>
  </svg>
</section>

<!-- letterhead option two -->
<section class="piece letterhead letterhead-two" aria-label="Letterhead option two">
  <p class="wordmark">Whitfield<small>&amp; Partners CPAs PSC</small></p>
  <p class="contact">
    <span><i></i>4815 Tillamore Ave. Suite 1, Owensboro, KY 42303</span>
    <span><i></i>270.555.0142</span>
    <span><i></i>www.wpfcpa.net</span>
  </p>
  <svg class="band" viewBox="0 0 308 425" preserveAspectRatio="none" aria-hidden="true">
    <path d="M170 425 C230 420 275 412 308 400 L308 425 Z" fill="var(--brand)"/>
    <path d="M215 425 C260 421 290 416 308 409 L308 425 Z" fill="var(--brand-deep)"/>
  </svg>
</section>

<!-- envelope back, blue flap -->
<section class="piece envelope env-back-blue" aria-label="Envelope back with blue flap">
  <svg class="flap" viewBox="0 0 380 122" preserveAspectRatio="none" aria-hidden="true">
    <defs>
      <linearGradient id="flapBlue" x1="0" y1="0" x2="0" y2="1">
        <stop offset="0" stop-color="var(--brand-light)"/>
        <stop offset="1" stop-color="var(--brand)"/>
      </linearGradient>
    </defs>
    <path d="M0 0 H380 V18 L200 66 Q190 69 180 66 L0 18 Z" fill="url(#flapBlue)"/>
  </svg>
  <p class="wordmark">Whitfield</p>
</section>

<!-- envelope back, grey flap -->
<section class="piece envelope env-back-grey" aria-label="Envelope back with grey flap">
  <svg class="flap" viewBox="0 0 380 122" preserveAspectRatio="none" aria-hidden="true">
    <path d="M0 0 H380 V16 L200 62 Q190 65 180 62 L0 16 Z" fill="var(--flap-grey)"/>
  </svg>
  <p class="wordmark">Whitfield</p>
</section>

<!-- envelope back, white flap -->
<section class="piece envelope env-back-white" aria-label="Envelope back with white flap">
  <svg class="flap" viewBox="0 0 380 122" preserveAspectRatio="none" aria-hidden="true">
    <path d="M0 0 L180 58 Q190 61 200 58 L380 0" fill="none" stroke="#d9dce2" stroke-width="1"/>
  </svg>
  <p class="wordmark">Whitfield</p>
</section>

<!-- envelope front -->
<section class="piece envelope env-front" aria-label="Envelope front">
  <p class="wordmark">Whitfield<small>&amp; Partners CPAs PSC</small></p>
  <p class="contact">4815 Tillamore Ave. Suite 1<br>Owensboro, KY 42303</p>
  <svg class="band" viewBox="0 0 380 94" preserveAspectRatio="none" aria-hidden="true">
    <path d="M170 94 C260 88 330 80 380 66 L380 94 Z" fill="var(--brand)"/>
    <path d="M240 94 C300 90 350 84 380 76 L380 94 Z" fill="var(--brand-deep)"/>
  </svg>
</section>

</body>
</html>
```